Home Health Care Agency Needs a Website (Seeking a PSD)

We need a user friendly website for a Home Health Care Agency. Our service is for the elderly and disabled. Frequently the busy professional middle-aged married daughter will use the website to arrange in-home care for an aging parent. Therefore, our website is primarily geared towards middle-aged women. In-home care is typically 24 hours a day so, a feeling of trustworthiness and security should be effectively conveyed. (Seeking a PSD- however, if you also offer coding, please let us know the cost.)

Target Market(s)

Frequently the busy professional middle-aged married daughter (possibly out of state) will use the website to arrange in-home care for an aging parent.

Industry/Entity Type

Security

Requirements
Must have
• Website must be clean, uncluttered and professional. The following menu pages are requested: Home, About Us, Services, Resources, FAQ, Employment & Contact.
Should not have
• Must not be too whimsical.

```html
<!DOCTYPE html>
<html lang="en">
<head>
<meta charset="utf-8">
<title>Harbor Lane Home Care</title>
<link rel="stylesheet" href="https://fonts.googleapis.com/css2?family=Open+Sans:wght@400;700&family=Questrial&display=swap">
<style>
:root{
  --page:#f3f5f6;
  --sky:#4fc6ec;
  --sky-deep:#1a90c9;
  --ink:#1e2226;
  --muted:#7a7f84;
  --footer:#3d4953;
  --footer-bottom:#4b5965;
  --footer-text:#e9edf0;
  --footer-head:#c9d0d5;
  --send:#1268b3;
  --accent:#d9261c;
  --field:#f1f1f2;
  --field-line:#c9ccd0;
}
*{box-sizing:border-box;margin:0;padding:0}
html,body{width:1200px;height:1104px;overflow:hidden}
body{background:var(--page);font-family:"Questrial",sans-serif;color:var(--ink);position:relative}
.abs{position:absolute}

.brand{left:152px;top:30px;display:flex;align-items:center;gap:10px}
.brand-mark{width:26px;height:26px;border-radius:50%;background:var(--sky)}
.brand-name{font-family:"Open Sans",sans-serif;font-weight:700;font-size:30px;color:var(--sky-deep);line-height:1.1;width:210px}
.header-contact{right:168px;top:58px;text-align:right}
.header-phone{font-family:"Open Sans",sans-serif;font-weight:700;font-size:22px;color:var(--sky);display:flex;align-items:center;justify-content:flex-end;gap:6px}
.header-email{font-size:21px;color:#5a5f64;display:flex;align-items:center;justify-content:flex-end;gap:6px;margin-top:2px}

.main-nav{left:0;top:126px;width:1200px;height:33px;background:var(--sky)}
.main-nav a{position:absolute;top:9px;color:#fff;text-decoration:none;font-size:13.5px;letter-spacing:.2px;text-transform:uppercase}

.hero{left:150px;top:160px;width:900px;height:372px;border:2px solid #6b7075;
  background:linear-gradient(100deg,#e9e4df 0%,#d8c2b2 25%,#f7f6f4 50%,#c9a58c 68%,#b9ddc8 90%,#e8f1ec 100%)}

.welcome-title{left:168px;top:557px;font-family:"Open Sans",sans-serif;font-weight:700;font-size:28px;color:var(--sky-deep);letter-spacing:.3px}
.welcome-photo{left:168px;top:611px;width:282px;height:191px;background:linear-gradient(120deg,#c9b7a6 0%,#6a4a7a 45%,#2c2f4a 75%,#7a6b5c 100%)}
.welcome-text{left:475px;top:610px;width:285px;font-size:13px;line-height:17.6px;color:var(--ink)}
.learn-more{left:476px;top:790px;font-size:13px;color:var(--accent);text-decoration:none;display:flex;align-items:center;gap:3px}

.quick-contact{left:803px;top:577px;width:230px;height:267px;background:#fff;border:1px solid #d5d9dc}
.quick-contact-head{height:31px;background:var(--sky);color:#fff;font-family:"Open Sans",sans-serif;font-weight:700;font-size:17px;padding:5px 0 0 58px;position:relative}
.quick-contact-head svg{position:absolute;left:16px;top:-14px}
.field{position:absolute;left:17px;width:191px;height:26px;background:var(--field);border:1px solid var(--field-line);font-size:11.5px;color:#9a9ea2;padding:5px 8px;letter-spacing:.3px}
.field svg{position:absolute;right:7px;top:6px}
.field-message{height:72px}
.send{position:absolute;left:17px;top:221px;width:191px;height:31px;background:var(--send);color:#fff;font-family:"Open Sans",sans-serif;font-size:16px;text-align:center;line-height:31px}

.site-footer{left:0;top:871px;width:1200px;height:200px;background:var(--footer)}
.footer-col{position:absolute;top:10px}
.footer-col h3{font-weight:400;font-size:19.5px;color:var(--footer-head);margin-bottom:10px;letter-spacing:.3px}
.footer-col ul{list-style:none}
.footer-col li{font-size:13.5px;color:var(--footer-text);line-height:21px;letter-spacing:.2px}
.footer-divider{position:absolute;top:28px;width:1px;height:152px;background:#1f262c}
.contact-line{display:flex;gap:6px;font-size:13.5px;color:var(--footer-text);line-height:16px;margin-bottom:16px;letter-spacing:.2px}
.contact-line svg{flex:none;margin-top:2px}
.copyright{left:0;top:1071px;width:1200px;height:33px;background:var(--footer-bottom);color:#dfe4e8;font-size:11.5px;text-align:center;line-height:33px;letter-spacing:.4px}
</style>
</head>
<body>

<header>
  <div class="abs brand">
    <span class="brand-mark"></span>
    <span class="brand-name">Harbor Lane Home Care</span>
  </div>
  <div class="abs header-contact">
    <div class="header-phone">
      <svg width="12" height="18" viewBox="0 0 12 18"><rect x="1" y="1" width="10" height="16" rx="2" fill="none" stroke="#7a7f84" stroke-width="2"/><circle cx="6" cy="14" r="1" fill="#7a7f84"/></svg>
      (555) 0142 300
    </div>
    <div class="header-email">
      <svg width="14" height="12" viewBox="0 0 14 12"><rect x="1" y="3" width="12" height="8" fill="none" stroke="#4fc6ec" stroke-width="1.6"/><path d="M1 3 L7 8 L13 3" fill="none" stroke="#4fc6ec" stroke-width="1.6"/></svg>
      info@harborlane.example
    </div>
  </div>
</header>

<nav class="abs main-nav">
  <a style="left:170px">Home</a>
  <a style="left:248px">About Us</a>
  <a style="left:356px">Services</a>
  <a style="left:457px">Resources</a>
  <a style="left:572px">FAQ</a>
  <a style="left:642px">Employment</a>
  <a style="left:771px">Contact Us</a>
</nav>

<div class="abs hero" role="img" aria-label="Photo of a smiling caregiver sharing a warm moment with an elderly woman"></div>

<h1 class="abs welcome-title">WELCOME TO HARBOR LANE HOME CARE</h1>
<div class="abs welcome-photo" role="img" aria-label="Photo of a nurse assisting an elderly woman seated in a wheelchair"></div>
<p class="abs welcome-text">Lorem Ipsum. Proin gravida nibh vel velit auctor aliquet. Aenean sollicitudin, lorem quis bibendum auctor, nisi elit consequat ipsum, nec sagittis sem nibh id elit. Duis sed odio sit am nibh vulputate cursus a sit amet mauris. Morbi accumsan ipsum velit. Nam nec tellus a odio tincidunt auctor a ornare odio. Sed non&nbsp; mauris vitae erat consequat auctor eu in elit. Class in aptent taciti sociosq ad litora torquent per conubia nostra, per</p>
<a class="abs learn-more">Learn more
  <svg width="8" height="8" viewBox="0 0 8 8"><path d="M1 1 L6 4 L1 7Z" fill="#c7c7c7"/></svg>
</a>

<aside class="abs quick-contact">
  <div class="quick-contact-head">
    <svg width="38" height="44" viewBox="0 0 38 44"><rect x="3" y="6" width="28" height="36" fill="#fff" stroke="#b9c0c6"/><path d="M8 16h18M8 22h18M8 28h14" stroke="#c6ccd1"/><path d="M14 30 L34 4" stroke="#555b61" stroke-width="2.5"/></svg>
    Quick Contact
  </div>
  <div class="field" style="top:51px">Enter your name
    <svg width="14" height="14" viewBox="0 0 14 14"><circle cx="7" cy="4.5" r="3.2" fill="#b3b7bb"/><path d="M1 14 C1 8 13 8 13 14Z" fill="#b3b7bb"/></svg>
  </div>
  <div class="field" style="top:84px">Enter your email
    <svg width="15" height="12" viewBox="0 0 15 12"><rect x="1" y="2" width="13" height="9" fill="none" stroke="#b3b7bb" stroke-width="1.6"/><path d="M1 2 L7.5 7 L14 2" fill="none" stroke="#b3b7bb" stroke-width="1.6"/></svg>
  </div>
  <div class="field" style="top:117px">Enter your phone
    <svg width="15" height="12" viewBox="0 0 15 12"><path d="M1 4 Q7.5 -1 14 4 L12 5 L10 3 L5 3 L3 5Z" fill="#b3b7bb"/><rect x="3" y="6" width="9" height="5" fill="#b3b7bb"/></svg>
  </div>
  <div class="field field-message" style="top:143px">Message</div>
  <div class="send">Send</div>
</aside>

<footer class="abs site-footer">
  <div class="footer-col" style="left:169px">
    <h3>Quick link</h3>
    <ul><li>Home</li><li>About Us</li><li>Services</li><li>Resources</li><li>FAQ</li><li>Employment</li><li>Contact Us</li></ul>
  </div>
  <div class="footer-divider" style="left:363px"></div>
  <div class="footer-col" style="left:485px">
    <h3>Terms &amp; Privacy</h3>
    <ul><li>Terms of Use</li><li>Privacy Policy</li><li>Collection of Information</li></ul>
  </div>
  <div class="footer-divider" style="left:771px"></div>
  <div class="footer-col" style="left:847px">
    <h3>Contact info</h3>
    <div class="contact-line">
      <svg width="13" height="20" viewBox="0 0 13 20"><path d="M6.5 1 C3 1 1 3.5 1 6.5 C1 10 6.5 19 6.5 19 C6.5 19 12 10 12 6.5 C12 3.5 10 1 6.5 1Z" fill="none" stroke="#9aa3aa" stroke-width="1.5"/><circle cx="6.5" cy="6.5" r="2" fill="#9aa3aa"/></svg>
      <span>Lorem Ipsum. met mauris.<br>Morbi accumsan ipsum velit.</span>
    </div>
    <div class="contact-line">
      <svg width="15" height="12" viewBox="0 0 15 12"><path d="M1 4 Q7.5 -1 14 4 L12 5 L10 3 L5 3 L3 5Z" fill="#b8c0c6"/><rect x="3" y="6" width="9" height="5" fill="#b8c0c6"/></svg>
      <span>(555) 0142 300</span>
    </div>
    <div class="contact-line">
      <svg width="15" height="12" viewBox="0 0 15 12"><rect x="1" y="2" width="13" height="9" fill="none" stroke="#b8c0c6" stroke-width="1.6"/><path d="M1 2 L7.5 7 L14 2" fill="none" stroke="#b8c0c6" stroke-width="1.6"/></svg>
      <span>info@harborlane.example</span>
    </div>
  </div>
</footer>
<div class="abs copyright">© 2013 HARBOR LANE HOME CARE, All rights reserved</div>

</body>
</html>
```